**** Web design project for BoltNet ****

For my ICT company BoltNet I need a website.

We design, build and host web-applications and we have our own CMS product. In the references part we want to show sample websites (thumbnails) + links.

It should look modern (WEB 2.0), rounded corners.

I want the following menu' s:
- Home
- Services
- References
- News
- About BoltNet
- Contact

Sample websites:
See attachments
http://www.vandoqa.com
http://www.greyfoxmanagement.nl

Reason: Want to take some time for feedback and improvements.

Reason: I'm waiting for a black background, with shadow and ambient light. You'll make a good chance!

Industry/Entity Type

It Company

Requirements
Must have
• - Fixed width (1024px), should fit on an IPad2
- Language selection English/Dutch
- Twitter/Facebook/LinkedIn/RSS icons
- Footer for Terms of use and Copyrights
- Search box
- 3 (or more) boxes for information i.e. news, blog or advertisements
Nice to have
• - Footer Site Map
- Contrasting background outside borders
- wide image (rotator) (with transperant sentence block)
- Shadow

```html
<!DOCTYPE html>
<html lang="en">
<head>
<meta charset="utf-8">
<title>BoltNet</title>
<link href="https://fonts.googleapis.com/css2?family=Arimo:wght@400;700&family=Jost:wght@700&display=swap" rel="stylesheet">
<style>
:root{
  --sky:#2b8ad8;
  --sky-dark:#1a6cc0;
  --band:#1f7bd6;
  --band-dark:#155fb3;
  --accent:#2a8fe0;
  --paper:#f3f3f3;
  --paper-top:#e6e6e6;
  --ink:#111;
  --text:#555;
  --rule:#c9c9c9;
  --photo-a:#3a2416;
  --photo-b:#8a5a2c;
}
*{margin:0;padding:0;box-sizing:border-box}
html,body{width:1200px;height:948px;overflow:hidden}
body{
  position:relative;
  font-family:"Arimo",Arial,sans-serif;
  background:radial-gradient(ellipse at center,var(--sky) 0%,var(--sky-dark) 100%);
}
.page{
  position:absolute;left:254px;top:0;width:699px;height:948px;
  background:linear-gradient(var(--paper-top),var(--paper) 180px,#e9e9e9);
  box-shadow:0 0 30px rgba(0,0,0,.45);
}
.top-band,.bottom-band{position:absolute;left:254px;width:699px;background:var(--band-dark)}
.top-band{top:0;height:10px}
.bottom-band{top:938px;height:10px}
.search{
  position:absolute;left:814px;top:12px;width:108px;height:20px;
  border-radius:4px;background:var(--band-dark);
  box-shadow:0 2px 3px rgba(0,0,0,.3);
}
.search span{
  position:absolute;left:4px;top:3px;width:86px;height:13px;border-radius:7px;
  border:1px solid #8cc4f2;background:var(--band);
  color:#fff;font-size:6px;font-weight:700;line-height:11px;padding-left:6px;
}
.search svg{position:absolute;right:3px;top:5px}
.logo{position:absolute;left:292px;top:46px;display:flex;align-items:center;gap:12px}
.logo i{width:52px;height:52px;border-radius:50%;background:var(--accent)}
.logo b{font-size:36px;font-weight:400;color:#5a6670;letter-spacing:1px}
.social{position:absolute;left:836px;top:67px;display:flex;gap:4px}
.social i{width:19px;height:19px;border-radius:4px;background:var(--band-dark);box-shadow:0 1px 2px rgba(0,0,0,.3)}
.nav{
  position:absolute;left:208px;top:128px;width:792px;height:33px;
  background:linear-gradient(var(--band),var(--band-dark));
  display:flex;align-items:center;padding-left:82px;gap:0;
}
.nav a{color:#fff;font-size:11px;font-weight:700;text-decoration:none;padding:5px 8px}
.nav a.current{background:var(--accent);border-radius:3px;padding:5px 14px;margin-right:4px;background:#3aa5ea}
.hero{
  position:absolute;left:288px;top:182px;width:432px;height:212px;
  background:#fff;padding:4px;box-shadow:0 1px 5px rgba(0,0,0,.35);
}
.hero div{width:100%;height:100%;background:linear-gradient(160deg,var(--photo-a),var(--photo-b) 60%,#5c1616)}
.intro{
  position:absolute;left:733px;top:182px;width:189px;height:212px;border-radius:4px;
  background:linear-gradient(var(--accent),var(--band-dark));padding:8px 9px;color:#fff;
  box-shadow:0 1px 5px rgba(0,0,0,.35);
}
.intro h1{font-family:"Jost",sans-serif;font-size:17px;line-height:19px;margin-bottom:4px}
.intro p{font-size:9.4px;line-height:12.5px}
.intro p b{white-space:nowrap}
.rule{position:absolute;left:288px;width:631px;height:1px;background:var(--rule)}
.col{position:absolute;width:186px}
.col h2,.refs-title{font-size:12px;font-weight:700;color:var(--ink);padding-bottom:6px;border-bottom:4px solid var(--accent);margin-bottom:8px}
.col h2::before,.refs-title::before,.more::before,.foot h3::before{content:"\2192";margin-right:9px;font-weight:400}
.col p{font-size:7.6px;line-height:13px;color:var(--text)}
.more{display:block;margin-top:14px;font-size:8px;font-weight:700;color:var(--accent)}
.ticks li{list-style:none;display:flex;gap:10px;font-size:7.6px;line-height:9.8px;color:var(--text);margin-bottom:10px}
.ticks li i{flex:0 0 9px;height:9px;background:#ccc;border:1px solid #aaa;position:relative}
.ticks li i::after{content:"";position:absolute;left:2px;top:0;width:3px;height:5px;border:solid #555;border-width:0 1px 1px 0;transform:rotate(40deg)}
.refs-title{position:absolute;left:288px;top:584px;border:0;font-size:12.5px}
.thumb{position:absolute;top:604px;width:186px;height:93px;background:linear-gradient(160deg,var(--photo-a),var(--photo-b) 60%,#5c1616)}
.thumb span{position:absolute;right:0;bottom:0;background:var(--accent);color:#fff;font-size:8px;font-weight:700;padding:3px 8px}
.foot{position:absolute;top:720px;width:186px}
.foot h3{font-size:8px;font-weight:700;color:var(--accent);margin-bottom:7px}
.foot p{font-size:7.6px;line-height:13px;color:var(--text)}
.copy{position:absolute;left:290px;top:918px;font-size:7.6px;color:var(--text)}
</style>
</head>
<body>
<div class="page"></div>
<div class="top-band"></div>
<div class="bottom-band"></div>

<div class="search"><span>SEARCH</span>
<svg width="8" height="8" viewBox="0 0 8 8"><circle cx="3.2" cy="3.2" r="2.4" fill="none" stroke="#cfe6fb" stroke-width="1"/><line x1="5" y1="5" x2="7.5" y2="7.5" stroke="#cfe6fb"/></svg></div>

<div class="logo"><i></i><b>BoltNet</b></div>
<div class="social" role="img" aria-label="Social network links"><i></i><i></i><i></i><i></i></div>

<nav class="nav">
<a class="current" href="#">Home</a><a href="#">Services</a><a href="#">References</a><a href="#">News</a><a href="#">About BoltNet</a><a href="#">Contact</a>
</nav>

<div class="hero"><div role="img" aria-label="Wide photo: a woman in a red gown seated in a hall of empty chairs"></div></div>
<div class="intro">
<h1>YOUR TITLE HERE</h1>
<p>Lorem ipsum dolor sit amet, consecte tur adipiscing elit. Pellentesque dapibus frin gilla odio, a consectetur Lorem ipsum dolor sit amet, consecte tur adipi­scing elit. Pellentesque dapibus frin gilla odio, a consectetur Lorem ipsum dolor sit amet, consecte tur adipiscing elit. Pellentesque dapibus frin gilla odio, a consectetur mi sodales vel. Maecenas ac ipsum metus, quis posuere lectus. Ut fringilla dui vel ante adipiscing sagittis. Maecenas justo nulla, venenatis ac lobortis sed, ornare eu sapien. <b>Continue reading »</b></p>
</div>

<div class="rule" style="top:413px"></div>

<section class="col" style="left:288px;top:426px">
<h2>ABOUT BOLTNET</h2>
<p>Lorem ipsum dolor sit amet, consectetur adipiscing elit. Pellentesque quis nulla id orci malesuada porta posuere quis massa. Nunc vitae purus non augue scelerisque ultricies vitae et velit. Sed vitae lectus id sem lobortis scelerisque. Praesent eget consequat libero.</p>
<a class="more">READ</a>
</section>
<section class="col" style="left:510px;top:426px">
<h2>SERVICES</h2>
<ul class="ticks">
<li><i></i>Lorem ipsum dolor sit amet, consectetur adipiscing elit. Pellentesque quis nulla id orci malesuada porta posuere quis massa.</li>
<li><i></i>Nunc vitae purus non augue scelerisque ultricies vitae et velit. Sed vitae lectus id sem lobortis scelerisque. Praesent eget consequat</li>
<li><i></i>Lorem ipsum dolor sit amet, consectetur adipiscing elit. Pellentesque quis nulla id orci malesuada porta posuere quis massa.</li>
</ul>
</section>
<section class="col" style="left:733px;top:426px">
<h2>TESTIMONIALS</h2>
<p>Lorem ipsum dolor sit amet, consectetur adipiscing elit. Pellentesque quis nulla id orci malesuada porta posuere quis massa. Nunc vitae purus non augue scelerisque ultricies vitae et velit. Sed vitae lectus id sem lobortis scelerisque.</p>
</section>

<div class="rule" style="top:572px"></div>
<h2 class="refs-title">REFERENCES</h2>
<div class="thumb" style="left:289px" role="img" aria-label="Reference website thumbnail"><span>VIEW →</span></div>
<div class="thumb" style="left:511px" role="img" aria-label="Reference website thumbnail"><span>VIEW →</span></div>
<div class="thumb" style="left:736px" role="img" aria-label="Reference website thumbnail"><span>VIEW →</span></div>

<div class="rule" style="top:710px"></div>
<footer>
<div class="foot" style="left:288px"><h3>SITE MAP</h3><p>Lorem ipsum dolor sit amet, consectetur adipiscing elit. Pellentesque quis nulla id orci malesuada porta posuere quis massa. Nunc vitae purus non augue scelerisque ultricies vitae et velit. Sed vitae lectus id sem lobortis scelerisque.</p></div>
<div class="foot" style="left:510px"><h3>TERMS OF USE</h3><p>Lorem ipsum dolor sit amet, consectetur adipiscing elit. Pellentesque quis nulla id orci malesuada porta posuere quis massa. Nunc vitae purus non augue scelerisque ultricies vitae et velit. Sed vitae lectus id sem lobortis scelerisque.</p></div>
<div class="foot" style="left:735px"><h3>CONTACT</h3><p>Lorem ipsum dolor sit amet, consectetur adipiscing elit. Pellentesque quis nulla id orci malesuada porta posuere quis massa. Nunc vitae purus non augue scelerisque ultricies vitae et velit. Sed vitae lectus id sem lobortis scelerisque.</p></div>
<p class="copy">© 2012 web site name. All Rights Reserved</p>
</footer>
</body>
</html>
```